Webdesign für Naturheilpraktiker gesucht
Zielgruppe
Ich arbeite im Gesundheitswesen als Naturheilpraktiker Traditionell Tibetische Medizin.
Verfüge aber über verschiedene Anwendungstechniken.
Die Zielgruppe sind alle Menschen die mehr als nur klassische Medizin wollen, die mit der klassischen Schulmedizin nicht mehr weiter kommen und einen alternativen Weg suchen. Menschen die neben der Schulmedizin noch einen anderen Weg suchen.
Menschen im Wellness und Fitnessbereich.
Ernährungsbewusste Menschen.
Sportler allgemein da ich über eine neue Technik verfüge (KERVO) die erst auf den Markt kommt und mit der verschiedene Beschwerden gelindert werden können.
Grob gesagt alles was mit Medizin, Komplementärmedizin, Gesundheit, Wellness, Sport usw zu tun hat.
Kompetenzen der Traditionell Tibetische Medizin:
- Massage als Gesundheitssystem oder als Wellness
- Ernährungsberatung
- tibetisches Yoga
- Lebensberatung
- Familienstellen
Aufgabenstellung
Der Firmennamen und das Logo bestehen.
In der Tradition der tibetischen Medizin ist vor allem Blau (Medizin Buddha) die Farben sind aber frei wählbar.
Es soll Vertrautheit, Geborgenheit und Wärme ausstrahlen.
Nicht zu feminin erscheinen.
Einfach ein paar Ideen
http://massagepraxis-wolfrin.example
http://www.himalheilkunde.example

```html
<!DOCTYPE html>
<html lang="de">
<head>
<meta charset="utf-8">
<title>LUNGTAHEIL – Naturheilpraxis</title>
<link rel="stylesheet" href="https://fonts.googleapis.com/css2?family=Open+Sans:wght@300;400;600&display=swap">
<style>
:root{
  --blue:#1d5aa3;
  --blue-dark:#174b8c;
  --teal:#2aa88a;
  --text:#333b44;
  --nav:#2f3a44;
  --footer:#4c4c4c;
  --footer-text:#6d6d6d;
  --white:#ffffff;
}
*{margin:0;padding:0;box-sizing:border-box}
html,body{width:1200px;height:818px;overflow:hidden}
body{font-family:"Open Sans",sans-serif;color:var(--text);background:var(--white);position:relative}
.hero{position:absolute;left:0;top:0;width:1200px;height:597px;
  background:linear-gradient(90deg,rgba(196,176,150,.55) 0%,rgba(214,206,190,.45) 25%,rgba(226,236,244,.4) 50%,rgba(236,243,250,.6) 100%),
  linear-gradient(180deg,#ffffff 0%,#eef4f8 30%,#e7eef2 70%,#e9eff3 100%)}
.hero-photo{position:absolute;inset:0}
.hero-veil{position:absolute;inset:0;background:linear-gradient(180deg,rgba(255,255,255,.9) 0%,rgba(255,255,255,.55) 18%,rgba(240,246,250,.55) 100%)}
.hero-strip{position:absolute;left:0;top:579px;width:1200px;height:18px;background:rgba(236,241,245,.8)}
.nav{position:absolute;top:25px;left:0;width:1200px;display:flex;justify-content:center;gap:19px;font-size:7px;letter-spacing:.3px;color:var(--nav);text-transform:uppercase}
.welcome{position:absolute;top:73px;left:0;width:1200px;text-align:center;font-weight:300;font-size:24px;color:var(--blue)}
.tagline{position:absolute;top:109px;left:0;width:1200px;text-align:center;font-weight:300;font-size:12px;color:var(--text)}
.divider{position:absolute;top:133px;left:562px}
.intro{position:absolute;top:157px;left:235px;width:730px;text-align:center;font-weight:300;font-size:12px;line-height:16px;color:#3a4b5c}
.service{position:absolute;width:170px}
.service h2{font-weight:300;font-size:16px;color:var(--blue);line-height:20px;margin-bottom:4px}
.service p{font-size:8.2px;line-height:12.6px;color:var(--text)}
.service a{color:var(--teal);text-decoration:underline}
.service.left{text-align:right}
.icon{position:absolute;width:38px;height:38px;border-radius:50%;background:var(--blue);border:3px solid #a9bfd8}
.emblem{position:absolute;left:512px;top:243px;width:176px;height:176px;border-radius:50%;border:2px solid #5b6470;display:flex;align-items:center;justify-content:center;font-size:15px;font-weight:400;color:var(--blue);letter-spacing:.5px}
.footer{position:absolute;left:0;top:597px;width:1200px;height:221px;background:var(--footer)}
.footer-mark{position:absolute;left:560px;top:30px;width:80px;height:80px;border-radius:50%;border:1.5px solid #cfcfcf;display:flex;align-items:center;justify-content:center;font-size:8px;color:#e0e0e0;letter-spacing:.3px}
.social{position:absolute;top:123px;left:510px;display:flex;gap:8px}
.social span{width:30px;height:30px;border-radius:50%;background:var(--white)}
.copyright{position:absolute;top:180px;left:0;width:1200px;text-align:center;font-size:8px;color:var(--footer-text)}
.to-top{position:absolute;left:1157px;top:166px;width:30px;height:30px;border:1.5px solid var(--white);display:flex;align-items:center;justify-content:center}
</style>
</head>
<body>
<section class="hero">
  <div class="hero-photo" role="img" aria-label="Unscharfe Landschaftsaufnahme eines Klosters an einem bewaldeten Berghang im Nebel"></div>
  <div class="hero-veil"></div>
  <div class="hero-strip"></div>

  <nav class="nav">
    <span>Home</span><span>Über mich</span><span>Tibetische Medizin</span><span>Angebot</span><span>Termine</span><span>Kontakt</span>
  </nav>

  <h1 class="welcome">Herzlich Willkommen bei LUNGTAHEIL</h1>
  <p class="tagline">NATURHEILPRAXIS TRADITIONELL TIBETISCHE MEDIZIN</p>
  <svg class="divider" width="76" height="16" viewBox="0 0 76 16">
    <line x1="2" y1="8" x2="24" y2="8" stroke="#2aa88a" stroke-width="1.2"/>
    <line x1="52" y1="8" x2="74" y2="8" stroke="#2aa88a" stroke-width="1.2"/>
    <circle cx="38" cy="8" r="5" fill="none" stroke="#2aa88a" stroke-width="1.2"/>
  </svg>
  <p class="intro">Muster Text Lorem ipsum dolor sit amet, consetetur sadipscing elitr, sed diam nonumy eirmod tempor invidunt ut labore et dolore magna aliquyam erat, sed diam voluptua.</p>

  <div class="service left" style="left:231px;top:239px">
    <h2>Tibetische Massage</h2>
    <p>Muster Text Cum sociis natoque penatibus et magnis dis parturient montesmus. Pro vel nibh et elit. <a>Mehr erfahren &gt;&gt;</a></p>
  </div>
  <span class="icon" style="left:419px;top:239px"></span>

  <div class="service left" style="left:231px;top:335px">
    <h2>Ernährungsberatung</h2>
    <p>Muster Text Cum sociis natoque penatibus et magnis dis parturient montesmus. Pro vel nibh et elit. <a>Mehr erfahren &gt;&gt;</a></p>
  </div>
  <span class="icon" style="left:419px;top:335px"></span>

  <div class="emblem">LUNGTAHEIL</div>

  <span class="icon" style="left:743px;top:239px"></span>
  <div class="service" style="left:799px;top:239px">
    <h2>Lebensberatung</h2>
    <p>Muster text Cum sociis natoque penatibus et magnis dis parturient montesmus. Pro vel nibh et elit. <a>Mehr erfahren &gt;&gt;</a></p>
  </div>

  <span class="icon" style="left:743px;top:335px"></span>
  <div class="service" style="left:799px;top:335px">
    <h2>Familienstellen</h2>
    <p>Muster Text Cum sociis natoque penatibus et magnis dis parturient montesmus. Pro vel nibh et elit. <a>Mehr erfahren &gt;&gt;</a></p>
  </div>

  <span class="icon" style="left:489px;top:447px"></span>
  <div class="service" style="left:545px;top:447px">
    <h2>Tibetisches Yoga</h2>
    <p>Muster Text Cum sociis natoque penatibus et magnis dis parturient montesmus. Pro vel nibh et elit. <a>Mehr erfahren &gt;&gt;</a></p>
  </div>
</section>

<footer class="footer">
  <div class="footer-mark">LUNGTAHEIL</div>
  <div class="social"><span></span><span></span><span></span><span></span><span></span></div>
  <p class="copyright">© 2018 LUNGTAHEIL. Alle Rechte vorbehalten</p>
  <div class="to-top">
    <svg width="10" height="6" viewBox="0 0 10 6"><polyline points="1,5 5,1 9,5" fill="none" stroke="#ffffff" stroke-width="1.4"/></svg>
  </div>
</footer>
</body>
</html>
```